Baby acupressure app for parents

We need an app for parents that teaches parents how to help them relieve their baby's imbalances (stomach ache, trouble sleeping etc.)

Please see the attached document (with info) and wireframes.

This project is urgent so please only participate if you're able to finish all screens within a few days after the contest is over.

Target Market(s)

Baby moms (20-40 years of age)

Industry/Entity Type

Baby Care

Colors
886aae
b768aa
e667a6
f68d4d
faa54b
fac994
f9ba93
f59195
fee18a

Requirements
Must have
• A high quality design that is both modern and very sleek and stylish.
Nice to have
• Simple animations to make the app "feel" like it's extreme high quality and make the user want to use it again and again
Should not have
• Sandwich menus

```html
<!DOCTYPE html>
<html lang="en">
<head>
<meta charset="utf-8">
<title>Sove Sødt – Article</title>
<link href="https://fonts.googleapis.com/css2?family=Lato:wght@400;700;900&family=Roboto:wght@400&display=swap" rel="stylesheet">
<style>
  :root {
    --purple-dark: #8447cf;
    --purple-light: #a24bd0;
    --heading: #7f5fa8;
    --body-text: #8c8c8c;
    --nav-icon: #b3b3b3;
    --nav-line: #e2e2e2;
    --white: #ffffff;
    --photo-light: #d9d6d3;
    --photo-mid: #b3aca6;
    --photo-dark: #6e6660;
  }
  * { margin: 0; padding: 0; box-sizing: border-box; }
  html, body { width: 675px; height: 1200px; overflow: hidden; background: var(--white); }
  body { position: relative; font-family: "Lato", sans-serif; }

  .app-header {
    position: absolute; top: 0; left: 0; width: 675px; height: 132px;
    background: linear-gradient(180deg, var(--purple-dark), var(--purple-light));
    color: var(--white);
  }
  .status-bar {
    position: absolute; top: 10px; left: 16px; right: 16px; height: 26px;
    display: flex; align-items: center; justify-content: space-between;
    font-family: "Roboto", sans-serif; font-size: 20px;
  }
  .status-left, .status-right { display: flex; align-items: center; gap: 8px; }
  .signal { display: flex; gap: 3px; }
  .signal span { width: 9px; height: 9px; border-radius: 50%; background: var(--white); }
  .signal span.empty { background: transparent; border: 1.5px solid var(--white); }
  .app-title {
    position: absolute; top: 67px; left: 0; width: 100%; text-align: center;
    font-weight: 900; font-size: 32px; letter-spacing: 1px; line-height: 1;
  }

  .hero { position: absolute; top: 132px; left: 0; width: 675px; height: 460px; }
  .play-button {
    position: absolute; left: 291px; top: 177px; width: 100px; height: 100px;
    border-radius: 50%; background: var(--white);
    box-shadow: 0 4px 14px rgba(0,0,0,0.25);
    display: flex; align-items: center; justify-content: center;
  }

  .article { position: absolute; top: 634px; left: 38px; width: 598px; }
  .article h1 { font-size: 27px; font-weight: 700; color: var(--heading); margin-bottom: 26px; }
  .article p {
    font-size: 14px; line-height: 23.4px; color: var(--body-text); margin-bottom: 24px;
  }

  .tab-bar {
    position: absolute; left: 0; top: 1085px; width: 675px; height: 115px;
    border-top: 1px solid var(--nav-line); background: var(--white);
  }
  .tab {
    position: absolute; top: 24px; width: 110px; margin-left: -55px;
    display: flex; flex-direction: column; align-items: center;
    font-family: "Roboto", sans-serif; font-size: 18px; color: var(--nav-icon);
  }
  .tab svg { height: 42px; margin-bottom: 12px; }
  .add-button {
    position: absolute; left: 286px; top: 1068px; width: 108px; height: 108px; border-radius: 50%;
    background: linear-gradient(180deg, var(--purple-dark), var(--purple-light));
    box-shadow: 0 6px 16px rgba(140, 70, 210, 0.3);
    display: flex; align-items: center; justify-content: center;
  }
</style>
</head>
<body>
  <header class="app-header">
    <div class="status-bar">
      <div class="status-left">
        <div class="signal"><span></span><span></span><span></span><span></span><span class="empty"></span></div>
        <span>Carrier</span>
        <svg width="20" height="16" viewBox="0 0 20 16"><path d="M10 15l3-4a5 5 0 0 0-6 0z M2 6a12 12 0 0 1 16 0l-2 2a9 9 0 0 0-12 0z" fill="#fff"/></svg>
      </div>
      <div class="status-right">
        <svg width="20" height="20" viewBox="0 0 20 20"><circle cx="10" cy="10" r="8" fill="none" stroke="#fff" stroke-width="1.6"/><rect x="7" y="9" width="6" height="5" fill="#fff"/></svg>
        <span>100%</span>
        <svg width="42" height="18" viewBox="0 0 42 18"><rect x="1" y="1" width="36" height="16" rx="3" fill="none" stroke="#fff" stroke-width="1.6"/><rect x="3.5" y="3.5" width="31" height="11" rx="1.5" fill="#fff"/><rect x="38.5" y="6" width="2.5" height="6" rx="1" fill="#fff"/></svg>
      </div>
    </div>
    <div class="app-title">SOVE SØDT</div>
  </header>

  <section class="hero">
    <svg width="675" height="460" viewBox="0 0 675 460" role="img" aria-label="Video still: a mother gently caring for her baby on a changing table">
      <defs>
        <linearGradient id="heroTone" x1="0" y1="0" x2="1" y2="1">
          <stop offset="0" stop-color="var(--photo-mid)"/>
          <stop offset="0.45" stop-color="var(--photo-light)"/>
          <stop offset="1" stop-color="var(--photo-dark)"/>
        </linearGradient>
      </defs>
      <path d="M0 0 H675 V358 Q337 548 0 358 Z" fill="url(#heroTone)"/>
    </svg>
    <div class="play-button">
      <svg width="36" height="42" viewBox="0 0 36 42"><path d="M4 3 L33 21 L4 39 Z" fill="#3d3d3d" stroke="#3d3d3d" stroke-width="4" stroke-linejoin="round"/></svg>
    </div>
  </section>

  <main class="article">
    <h1>What is Lorem Ipsum?</h1>
    <p>Lorem Ipsum is simply dummy text of the printing and typesetting industry. Lorem Ipsum has been the industry's standard dummy text ever since the 1500s, when an unknown printer took a galley of type and scrambled it to make a type specimen book. It has survived not only five centuries, but also the leap into electronic typesetting, remaining essentially unchanged.</p>
    <p>Lorem Ipsum is simply dummy text of the printing and typesetting industry. Lorem Ipsum has been the industry's standard dummy text ever since the 1500s, when an unknown printer took a galley of type and scrambled it to make a type specimen book. It has survived not only five centuries, but also the leap into electronic typesetting, remaining essentially unchanged.</p>
    <p>Lorem Ipsum is simply dummy text of the printing and typesetting industry. Lorem Ipsum has been the industry's standard dummy text ever since the 1500s, when an unknown printer took a galley of type and scrambled it to make a type specimen book. It has survived not only five centuries, but also the leap into electronic typesetting, remaining essentially unchanged.</p>
  </main>

  <nav class="tab-bar">
    <div class="tab" style="left:86px">
      <svg width="40" height="42" viewBox="0 0 40 42"><path d="M3 19 L20 4 L37 19 M7 16 V38 H16 V26 H24 V38 H33 V16" fill="none" stroke="var(--nav-icon)" stroke-width="2.4" stroke-linejoin="round"/></svg>
      Home
    </div>
    <div class="tab" style="left:207px">
      <svg width="36" height="42" viewBox="0 0 36 42"><circle cx="18" cy="12" r="7" fill="none" stroke="var(--nav-icon)" stroke-width="3"/><path d="M3 36 Q3 24 18 24 Q33 24 33 36 Z" fill="none" stroke="var(--nav-icon)" stroke-width="3" stroke-linejoin="round"/></svg>
      Problems
    </div>
    <div class="tab" style="left:468px">
      <svg width="42" height="44" viewBox="0 0 42 44"><g fill="none" stroke="var(--nav-icon)" stroke-width="2.4"><circle cx="33" cy="8" r="6"/><circle cx="9" cy="22" r="6"/><circle cx="33" cy="36" r="6"/><path d="M14 19 L28 11 M14 25 L28 33"/></g></svg>
      Share
    </div>
    <div class="tab" style="left:599px">
      <svg width="28" height="50" viewBox="0 0 28 50"><circle cx="17" cy="6" r="5.5" fill="var(--nav-icon)"/><path d="M6 18 H20 L17 42 Q17 45 21 45 L20 48 H5 L6 45 Q10 45 10 42 L12 22 H6 Z" fill="var(--nav-icon)"/></svg>
      About
    </div>
  </nav>
  <div class="add-button">
    <svg width="30" height="30" viewBox="0 0 30 30"><path d="M15 2 V28 M2 15 H28" stroke="#fff" stroke-width="3.4" stroke-linecap="round"/></svg>
  </div>
</body>
</html>
```